Redesign Of Hotel Coupon/Voucher 8.5 x 11

I would like to redesign my voucher.

Please provide me a color flyer design but one that would be easy on printing costs...for example printing from home computer/printer.

I would like to see some color designs...maybe some black and white and also full graphics and even basic like the plum rook voucher I provided as a sample. The 2 night hotel stay is the voucher I need to redesign...

Target Market(s)

Consumers

Industry/Entity Type

Hotel

Requirements
Must have
• exact text in current designs---look official, credible and trust worthy
Nice to have
• I would like to redesign my voucher.
• Please provide me a color flyer design but one that would be easy on printing costs...for example printing from home computer/printer.
• I would like to see some color designs...maybe some black and white and also full graphics and even basic like the plum rook voucher I provided as a sample. The 2 night hotel stay is the voucher I need to redesign...
Should not have

```html
<!DOCTYPE html>
<html lang="en">
<head>
<meta charset="utf-8">
<title>2 Night Hotel Stay Voucher</title>
<link href="https://fonts.googleapis.com/css2?family=Anton&family=Lato:wght@400;700;900&family=Parisienne&family=Arimo:wght@400;700&display=swap" rel="stylesheet">
<style>
  :root {
    --ink: #111111;
    --charcoal: #3a3a3a;
    --mid-grey: #6e6e6e;
    --soft-grey: #a9a9a9;
    --pale-grey: #e4e4e4;
    --paper: #ffffff;
    --band: #0d0d0d;
  }
  html, body { margin: 0; padding: 0; overflow: hidden; background: var(--paper); }
  .voucher {
    position: relative; width: 881px; height: 1200px; overflow: hidden;
    background: linear-gradient(90deg, #8f8f8f 0%, #c9c9c9 30%, #e9e9e9 60%, #f4f4f4 100%);
    font-family: 'Lato', sans-serif; color: var(--ink);
  }
  .hero { position: absolute; left: 0; top: 0; width: 881px; height: 380px; }

  .offer-panel {
    position: absolute; left: 0; top: 356px; width: 350px; height: 532px;
    background: var(--paper);
  }
  .offer-edge { position: absolute; left: 0; top: 860px; width: 352px; height: 36px; }
  .offer-title-lead {
    position: absolute; left: 38px; top: 418px; margin: 0;
    font-family: 'Anton', sans-serif; font-size: 96px; line-height: 1; letter-spacing: -1px;
    color: var(--soft-grey); text-shadow: -4px 3px 0 var(--ink);
  }
  .offer-title {
    position: absolute; left: 38px; top: 522px; margin: 0;
    font-family: 'Anton', sans-serif; font-size: 72px; line-height: 1; color: var(--ink);
  }
  .destinations {
    position: absolute; left: 24px; top: 632px; width: 312px; margin: 0;
    font-size: 11.4px; line-height: 13.5px; font-weight: 700; text-align: justify; color: var(--ink);
  }

  .terms-panel {
    position: absolute; left: 350px; top: 330px; width: 531px; height: 545px;
    background: linear-gradient(90deg, #9c9c9c 0%, #cfcfcf 35%, #ececec 70%, #f6f6f6 100%);
  }
  .terms-heading {
    position: absolute; left: 605px; top: 346px; margin: 0;
    font-family: 'Parisienne', cursive; font-weight: 400; font-size: 31px; color: var(--ink);
  }
  .terms-column {
    position: absolute; top: 388px; width: 252px; margin: 0;
    font-size: 10.3px; line-height: 13.3px; font-weight: 700; text-align: justify; color: var(--ink);
  }
  .terms-column.first { left: 362px; }
  .terms-column.second { left: 624px; }

  .redeem-intro {
    position: absolute; left: 112px; top: 930px; width: 222px; margin: 0;
    font-size: 11px; line-height: 13.4px; font-weight: 700; color: var(--charcoal);
  }
  .redeem-box {
    position: absolute; left: 122px; top: 1006px; width: 210px; height: 80px;
    border: 1.5px solid var(--ink); box-sizing: border-box; padding: 7px 0 0 10px;
  }
  .redeem-box ul { list-style: none; margin: 0; padding: 0; }
  .redeem-box li { position: relative; padding-left: 18px; font-size: 11px; font-weight: 700; line-height: 13.5px; margin-bottom: 6px; color: var(--charcoal); }
  .redeem-box li svg { position: absolute; left: 0; top: 2px; }
  .redeem-box .site { color: var(--ink); }
  .redemption-address {
    position: absolute; left: 122px; top: 1100px; width: 210px; margin: 0;
    text-align: center; font-size: 11px; line-height: 15px; font-weight: 700; color: var(--charcoal);
  }
  .certificate-band {
    position: absolute; left: 0; top: 1140px; width: 350px; height: 60px;
    background: var(--band); color: var(--paper); box-sizing: border-box; padding: 8px 0 0 34px;
    font-size: 16px; font-weight: 700; line-height: 23px;
  }

  .order-form {
    position: absolute; left: 347px; top: 893px; width: 534px; height: 307px;
    background: var(--paper); font-family: 'Arimo', sans-serif; color: var(--ink);
  }
  .form-heading { position: absolute; margin: 0; font-size: 10.5px; font-weight: 700; }
  .field { position: absolute; display: flex; align-items: flex-end; font-size: 10px; font-weight: 700; height: 14px; }
  .field .line { border-bottom: 1px solid var(--ink); margin-left: 4px; height: 11px; }
  .pay-option { position: absolute; display: flex; align-items: center; font-size: 10px; font-weight: 700; }
  .pay-option .box { width: 14px; height: 13px; background: #b8b8b8; border: 1px solid var(--mid-grey); margin-right: 5px; }
  .form-note { position: absolute; left: 240px; margin: 0; font-size: 7px; line-height: 10px; width: 290px; }
</style>
</head>
<body>
<main class="voucher">

  <svg class="hero" viewBox="0 0 881 380" role="img" aria-label="Black and white photograph of an elegant hotel room with a made bed, armchair, curtains and desk">
    <defs>
      <linearGradient id="roomTone" x1="0" y1="0" x2="1" y2="1">
        <stop offset="0" stop-color="#f1f1f1"/>
        <stop offset="0.45" stop-color="#a9a9a9"/>
        <stop offset="1" stop-color="#3c3c3c"/>
      </linearGradient>
    </defs>
    <path d="M0 0 H881 V300 C760 300 640 330 470 352 C300 372 150 352 0 346 Z" fill="url(#roomTone)"/>
    <path d="M0 346 C150 352 300 372 470 352 C640 330 760 300 881 300 V338 C720 332 600 355 430 372 C260 388 120 372 0 368 Z" fill="#5a5a5a"/>
  </svg>

  <div class="terms-panel"></div>
  <div class="offer-panel"></div>
  <svg class="offer-edge" viewBox="0 0 352 36">
    <polygon points="0,0 352,0 352,6 240,26 0,6" fill="#ffffff"/>
    <polyline points="0,8 240,28 352,8" fill="none" stroke="#1a1a1a" stroke-width="3"/>
  </svg>

  <h1 class="offer-title-lead">2 Night</h1>
  <h2 class="offer-title">Hotel Stay:</h2>
  <p class="destinations">Destinations Available: Anaheim, CA--Atlanta, GA--Atlantic City, NJ--Branson, MO--Cancun, MX--Charleston, SC--Coeur d' Alene, ID--Daytona Beach, FL--Destin, FL--Ft. Lauderdale, FL--Ft. Meyers, FL--Gatlinburg, TN--Hilton Head, SC--Honolulu, HI--Kissimmee, FL--Lake Tahoe, CA--Las Vegas, NV--Myrtle Beach, SC--Niagara Falls/Buffalo Area, NY--Orlando, FL--Ormond Beach, FL--Palm Springs, CA--Pigeon Forge, TN--St. Petersburg, FL--San Antonio, TX--San Diego, CA--San Francisco, CA--Sedona, AZ--Sonoma Wine Country, CA--St. George, UT--Tampa, FL--Williamsburg, VA--Wisconsin Dells, WI--Tallahassee, FL--Augusta, GA--Columbia, SC--New York, NY--Florence, SC--Washington, D.C.--Chicago, IL--Salt Lake City, UT--Hollywood, CA--Dayton, OH--Tucson, AZ--Niagra Falls, ON/CAN--Seattle, WA--Portland, OR--Antioch, CA--San Mateo, CA--Brunswick, GA--Nashville, TN</p>

  <h3 class="terms-heading">Terms &amp; Condition :</h3>
  <p class="terms-column first">This certificate will be considered void if bartered or purchased for legal tender by the recipient. This certificate is valid for a reservation request form offering 2 adults 21 years of age and older plus up to 2 children under the age of 18, 2 nights of hotel accommodations in the city of their choice of available cities. The cost to activate this certificate to receive the reservation request form is just a one-time non-refundable $14.95 processing fee. The cost upon requesting reservations is just a tax &amp; fee deposit of $33 per night. Taxes &amp; fees usually range from $12-$33 per night depending on when and where you travel to. If the taxes &amp; fees are less than the $33 per night the difference will be refunded after travel is completed. 30 days advance reservation notice is required. In order to guarantee that you will show up to your booked reservation you will be required to pay a REFUNDABLE $50 "Reservation Guarantee Deposit". If you send in your travel dates, etc and you do not end up traveling then the reservation guarantee deposit will not be refundable. 7 days before and after holidays and conventions are not available. This offer is valid 7 days a week subject to availability. Friday and Saturday nights will require a surcharge of $20 per night. A $5 per person per night surcharge is enforced for each child up to 2 children under the age of 18.This offer is not valid for group travel.</p>
  <p class="terms-column second">The recipient of this certificate is responsible for all expenses including but not limited to: transfers, food, gratuities, all pertinent fees, taxes, hotel surcharges, resort fees and any other miscellaneous expenses. If you activate this certificate online you will be able to instantly print your reservation request form. If you cannot print your own reservation request form we will mail it to you. You should receive it in the mail within 14 days. This certificate cannot be combined with any other promotional vacation offer. The expiration date on this certificate pertains only to activation of this certificate and not actual travel. You must activate this certificate by the expiration date printed on this certificate in order to receive the reservation request form. You must fill out the reservation request form with your destination choices and arrival dates and mail it to our fulfillment department within 6 months after activation, however travel can be completed within 12 months after activation. You will be required to give the travel agency multiple arrival dates and destinations. Only one 2 Night Hotel certificate Per Household Per Year. This certificate has no cash surrender value, void if discontinued and where prohibited by law. The terms of this offer are subject to change without notice. Do not rely upon representations other than what is printed on this certificate or the reservation request form. CST # 5530418</p>

  <p class="redeem-intro">Simply fill out the form on this certificate and enclose payment of U.S. $14.95. Velora, Northcard, Anchor Express, Dovetail, Debit Card, Check Card, Check &amp; Money Orders are all accepted.</p>
  <div class="redeem-box">
    <ul>
      <li><svg width="11" height="9" viewBox="0 0 11 9"><path d="M1 5 L4 8 L10 1" fill="none" stroke="#111" stroke-width="1.8"/></svg>For expedited redemption go to:<br><span class="site">www.PlumRookStays.com</span></li>
      <li><svg width="11" height="9" viewBox="0 0 11 9"><path d="M1 5 L4 8 L10 1" fill="none" stroke="#111" stroke-width="1.8"/></svg>Fax* certificate to: 1-888-555-0142</li>
      <li><svg width="11" height="9" viewBox="0 0 11 9"><path d="M1 5 L4 8 L10 1" fill="none" stroke="#111" stroke-width="1.8"/></svg>Mail* to:</li>
    </ul>
  </div>
  <p class="redemption-address">Redemption Center<br>4120 Alder Crest Ave Ste B #210</p>
  <div class="certificate-band">Certificate ID: -10002<br>Expiration Date: 04/08/2017</div>

  <section class="order-form">
    <h4 class="form-heading" style="left:16px;top:10px;">BILLING INFORMATION</h4>
    <div class="field" style="left:16px;top:26px;">Name:<span class="line" style="width:165px;margin-left:20px"></span></div>
    <div class="field" style="left:16px;top:43px;">Address:<span class="line" style="width:165px;margin-left:7px"></span></div>
    <div class="field" style="left:16px;top:60px;">City:<span class="line" style="width:165px;margin-left:27px"></span></div>
    <div class="field" style="left:16px;top:77px;">State:<span class="line" style="width:165px;margin-left:21px"></span></div>
    <div class="field" style="left:16px;top:94px;">Zip Code:<span class="line" style="width:165px;margin-left:5px"></span></div>
    <div class="field" style="left:16px;top:111px;">Country:<span class="line" style="width:165px;margin-left:8px"></span></div>
    <div class="field" style="left:16px;top:128px;">Phone:<span class="line" style="width:165px;margin-left:17px"></span></div>
    <div class="field" style="left:16px;top:145px;">Email:<span class="line" style="width:165px;margin-left:19px"></span></div>

    <h4 class="form-heading" style="left:16px;top:172px;">SHIPPING INFORMATION</h4>
    <div class="field" style="left:16px;top:189px;">Name:<span class="line" style="width:165px;margin-left:20px"></span></div>
    <div class="field" style="left:16px;top:206px;">Address:<span class="line" style="width:165px;margin-left:7px"></span></div>
    <div class="field" style="left:16px;top:223px;">City:<span class="line" style="width:165px;margin-left:27px"></span></div>
    <div class="field" style="left:16px;top:240px;">State:<span class="line" style="width:165px;margin-left:21px"></span></div>
    <div class="field" style="left:16px;top:257px;">Zip Code:<span class="line" style="width:165px;margin-left:5px"></span></div>
    <div class="field" style="left:16px;top:274px;">Country:<span class="line" style="width:165px;margin-left:8px"></span></div>

    <h4 class="form-heading" style="left:240px;top:12px;">PAYMENT INFORMATION</h4>
    <div class="field" style="left:240px;top:28px;">Payment Method:</div>
    <div class="pay-option" style="left:262px;top:50px;"><span class="box"></span>Check</div>
    <div class="pay-option" style="left:330px;top:50px;"><span class="box"></span>Money Order</div>
    <div class="pay-option" style="left:262px;top:71px;"><span class="box"></span>Velora</div>
    <div class="pay-option" style="left:330px;top:71px;"><span class="box"></span>Northcard</div>
    <div class="pay-option" style="left:262px;top:92px;"><span class="box"></span>Anchor</div>
    <div class="pay-option" style="left:330px;top:92px;"><span class="box"></span>Dovetail Card</div>
    <div class="field" style="left:240px;top:116px;">Name On Card:<span class="line" style="width:165px;margin-left:14px"></span></div>
    <div class="field" style="left:240px;top:133px;">Card # (16 digits):<span class="line" style="width:165px"></span></div>
    <div class="field" style="left:240px;top:150px;">Expiration Date:<span class="line" style="width:22px;margin-left:8px"></span><span style="margin:0 6px">/</span><span class="line" style="width:66px;margin-left:0"></span></div>
    <div class="field" style="left:240px;top:167px;">CV2#**:<span class="line" style="width:50px;margin-left:10px"></span></div>
    <div class="field" style="left:240px;top:195px;">I agree to terms and conditions</div>
    <div class="field" style="left:240px;top:212px;">Signature:<span class="line" style="width:198px;margin-left:8px"></span></div>
    <p class="form-note" style="top:235px;">"Redemption Center" will appear on your billing statement.<br>Make checks and money orders payable to: "Redemption Center"<br>* You will receive your information by mail within 10 days.<br>** Last 3 digits on back of card (4 digits on front of Anchor).</p>
  </section>

</main>
</body>
</html>
```